New branding for a sponsored social ad network

We're seeking a new corporate branding for our sponsored social ad network.

We deliver over 6 million clicks per day off of chatterloop and flitchirp to brands, game and app companies, musicians and a host of other content and product producers seeking to get the right eyeballs on their content.

Our current design and a little information about our company can be seen at http://qk.zv/pmTGsa

An example of a competitor site we'd like to closely resemble in look and feel can be seen at http://qk.zv/84HnQ3x

It Company

```html
<!DOCTYPE html>
<html lang="en">
<head>
<meta charset="utf-8">
<title>Murmurads</title>
<link rel="stylesheet" href="https://fonts.googleapis.com/css2?family=Source+Sans+3:wght@400;600;700&family=Arimo:wght@700&display=swap">
<style>
:root{
  --header:#2f2f2f;
  --dark:#404040;
  --footer:#333333;
  --brand:#1eb4e8;
  --lime:#7ed321;
  --lime-band:#7fd11a;
  --pale:#e0f6fd;
  --ink:#333333;
  --btn-dark:#2e3a45;
  --orange:#fd9a2a;
  --yellow:#fde65a;
  --green:#7dd33b;
  --blue:#0cbdf0;
}
*{box-sizing:border-box;margin:0;padding:0}
html,body{width:1108px;height:1200px;overflow:hidden}
body{position:relative;font-family:"Source Sans 3",Arial,sans-serif;background:var(--footer);color:var(--ink)}
.abs{position:absolute}
.site-header{left:0;top:0;width:1108px;height:87px;background:var(--header)}
.brand{left:120px;top:20px;font-size:35px;font-weight:600;color:var(--brand);line-height:1;display:flex;align-items:center;gap:5px}
.brand-dot{width:12px;height:12px;border-radius:50%;background:var(--lime);display:inline-block;margin-top:-16px}
.main-nav{top:36px;left:342px;font-size:13px;font-weight:600;color:#fff;letter-spacing:.3px;white-space:nowrap}
.main-nav span{position:absolute;top:0}
.main-nav b{color:var(--lime);font-weight:600}
.util-nav{top:35px;right:120px;font-size:12px;color:var(--brand);letter-spacing:.2px;white-space:nowrap}
.util-nav span{color:#888;margin:0 7px}
.hero{left:0;top:87px;width:1108px;height:424px;background:linear-gradient(180deg,#0a4fc7 0%,#2a7fe8 30%,#ffffff 50%,#3a9ff0 62%,#0b5ed8 85%,#0c7ee2 100%)}
.hero-card{left:120px;top:85px;width:499px;height:242px;background:rgba(255,255,255,.82)}
.hero-brand{position:absolute;left:18px;top:8px;font-size:38px;font-weight:600;color:var(--brand);display:flex;align-items:center;gap:5px;line-height:1.1}
.hero-copy{position:absolute;left:19px;top:71px;width:470px;font-size:22px;line-height:27.7px;color:#3d3d3d}
.btn-learn{position:absolute;left:19px;top:197px;width:117px;height:31px;line-height:31px;text-align:center;background:var(--btn-dark);color:#fff;font-size:14px;font-weight:600;border-radius:3px;letter-spacing:.3px}
.hero-dots{left:905px;top:384px;display:flex;gap:4px}
.hero-dots i{width:17px;height:17px;border-radius:50%;background:rgba(255,255,255,.55);display:block}
.hero-dots i:first-child{background:#fff}
.contact-band{left:0;top:511px;width:1108px;height:129px;background:var(--lime-band)}
.band-title{position:absolute;top:16px;font-size:25px;font-weight:600;color:#2c4f14;letter-spacing:.5px;white-space:nowrap}
.call-lines{position:absolute;left:120px;top:48px;font-size:20px;font-weight:600;color:#fff;line-height:31px;letter-spacing:.3px}
.field{position:absolute;top:51px;width:207px;height:31px;background:#fff;border-radius:4px;font-size:13px;color:#a8a8a8;padding:7px 14px;letter-spacing:.3px}
.forgot{position:absolute;left:797px;top:96px;font-size:13px;font-weight:600;color:#1468c8;white-space:nowrap}
.btn-signin{position:absolute;left:914px;top:91px;width:74px;height:26px;background:linear-gradient(#1fa0ea,#0c6ad0);border-radius:3px;color:#fff;font-size:13px;font-weight:600;text-align:center;line-height:26px}
.how{left:0;top:640px;width:1108px;height:278px;background:var(--pale)}
.how-col{position:absolute;top:15px;width:440px;text-align:center}
.how-col h2{font-size:25px;font-weight:600;color:#333;letter-spacing:.4px}
.steps{position:relative;height:120px;margin-top:18px}
.step{position:absolute;top:0;width:105px;height:105px;border-radius:50%;display:flex;align-items:center;justify-content:center;text-align:center;font-family:Arimo,Arial,sans-serif;font-weight:700;font-size:14.5px;line-height:21px;color:#fff;mix-blend-mode:multiply}
.s1{background:var(--orange)}.s2{background:var(--yellow)}.s3{background:var(--green)}.s4{background:var(--blue)}
.how-col p{font-size:12px;line-height:18.5px;color:#333;padding:0 8px}
.story{left:0;top:918px;width:1108px;height:234px;background:var(--dark)}
.story h3{position:absolute;left:120px;top:18px;font-size:21px;font-weight:600;color:#7fd6f5;letter-spacing:.3px}
.story p{position:absolute;left:120px;top:53px;width:375px;font-size:12.3px;line-height:21.3px;color:#e6e6e6}
.btn-read{position:absolute;left:121px;top:179px;background:#9ee6fb;color:#2a2a2a;font-size:11.5px;font-weight:600;padding:5px 7px;border-radius:3px}
.social-box{left:545px;top:16px;width:443px;height:209px;background:#fff;border:1px solid #c8ccd6;font-family:Arial,sans-serif;overflow:hidden}
.sb-head{height:17px;background:#edeff4;border-bottom:1px solid #d8dbe2;font-size:10.5px;color:#222;padding:2px 2px}
.sb-page{display:flex;align-items:center;gap:6px;padding:9px 7px;height:57px;border-bottom:1px solid #e4e4e4}
.sb-logo{font-size:8px;color:var(--brand);font-weight:700;width:40px;overflow:hidden}
.sb-name{font-size:11px;color:#3b5998;font-weight:700}
.sb-like{margin-top:3px;border:1px solid #c6c8cc;background:#f2f2f2;font-size:9px;color:#333;padding:2px 5px;display:inline-block}
.sb-count{font-size:9px;color:#333;padding:6px 5px 5px}
.sb-count b{color:#3b5998;font-weight:400}
.faces{display:grid;grid-template-columns:repeat(10,40px);gap:3px 2px;padding:0 6px}
.faces i{height:40px;display:block}
.sb-foot{position:absolute;bottom:0;left:0;right:0;height:20px;border-top:1px solid #e4e4e4;font-size:8px;color:#555;padding:5px 8px;display:flex;gap:4px;align-items:center}
.sb-foot i{width:9px;height:9px;background:#3b5998;display:block}
.site-footer{left:0;top:1152px;width:1108px;height:48px;background:var(--footer)}
.legal{position:absolute;left:121px;top:16px;font-size:11.5px;color:#bbb}
.legal b{color:#fff;font-weight:400}
.legal span{margin:0 5px}
.social{position:absolute;left:878px;top:6px;display:flex;gap:5px}
.social i{width:34px;height:34px;border-radius:50%;background:#8a8a8a;display:block}
</style>
</head>
<body>
<header class="abs site-header">
  <div class="abs brand">Murmurads<span class="brand-dot"></span></div>
  <nav class="abs main-nav"><span style="left:0"><b>SIGNUP</b> AS PUBLISHERS</span><span style="left:186px"><b>SIGNUP</b> AS ADVERTISERS</span></nav>
  <nav class="abs util-nav">ABOUT US<span>|</span>SIGN UP<span>|</span>LOGIN</nav>
</header>

<section class="abs hero" role="img" aria-label="Business people in silhouette shaking hands in front of a blue world map">
  <div class="abs hero-card">
    <div class="hero-brand">Murmurads<span class="brand-dot"></span></div>
    <p class="hero-copy">Murmurads is the Rex Ironside of social traffic,<br>our publishers reach over 200 million unique<br>consumers in 80 countries, impressed?<br>Yeah that is kind of cool actually...</p>
    <span class="btn-learn">LEARN MORE</span>
  </div>
  <div class="abs hero-dots"><i></i><i></i><i></i><i></i></div>
</section>

<section class="abs contact-band">
  <h2 class="band-title" style="left:120px">CALL US!</h2>
  <p class="call-lines">We totally speak English (855)-MURMURAD<br>(687-6872)</p>
  <h2 class="band-title" style="left:564px">SIGN IN</h2>
  <div class="field" style="left:561px">Email</div>
  <div class="field" style="left:782px">Password</div>
  <span class="forgot">Forgot Password ?</span>
  <span class="btn-signin">Sign In</span>
</section>

<section class="abs how">
  <div class="how-col" style="left:112px">
    <h2>How it Works for Publishers</h2>
    <div class="steps">
      <div class="step s1" style="left:36px">Sign Up</div>
      <div class="step s2" style="left:126px">Pick<br>Your<br>Products</div>
      <div class="step s3" style="left:212px">Publish<br>Your<br>Findings</div>
      <div class="step s4" style="left:299px">Make<br>Money</div>
    </div>
    <p>Whether you have 100 friends/followers on chatterloop and flitchirp or 100,000+ you can earn great money posting fun and interesting content from brands and sites you already love and talk about anyway, so what are you waiting for?</p>
  </div>
  <div class="how-col" style="left:556px">
    <h2>How it Works for Advertisers</h2>
    <div class="steps">
      <div class="step s1" style="left:32px">Create<br>an<br>Account</div>
      <div class="step s2" style="left:122px">Add<br>Your<br>Content</div>
      <div class="step s3" style="left:213px">Create a<br>Weekly<br>Budget</div>
      <div class="step s4" style="left:303px">Receive<br>Relevant<br>Clicks</div>
    </div>
    <p>ou want to reach relevant consumers right? Right. Well there's no better customer than one that was referred to you by someone they like and trust, that's a fact Jack. With Murmurads you can target huge audiences by interests and other demographics....</p>
  </div>
</section>

<section class="abs story">
  <h3>True Story</h3>
  <p>TuneHopper.com wanted to promote their new free app that allows users to download streamora videos as music files. Murmurads traffic resulted in over 1.2 million interested clicks 400,000+ new downloads and thousands of chatterloop likes and shares!</p>
  <span class="btn-read">READ MORE</span>
  <div class="abs social-box">
    <div class="sb-head">Find us on chatterloop</div>
    <div class="sb-page">
      <span class="sb-logo">Murmurads</span>
      <div><div class="sb-name">Murmurads</div><span class="sb-like">Like</span></div>
    </div>
    <div class="sb-count">2,994 people like <b>Murmurads</b>.</div>
    <div class="faces" role="img" aria-label="Grid of member profile thumbnails">
      <i style="background:#a0785a"></i><i style="background:#c9583c"></i><i style="background:#8a7060"></i><i style="background:#6a4a3a"></i><i style="background:#b8b8c0"></i><i style="background:#7a8a6a"></i><i style="background:#5a4a7a"></i><i style="background:#dfe3ea"></i><i style="background:#8a9a8a"></i><i style="background:#c87a8a"></i>
      <i style="background:#6a5040"></i><i style="background:#dfe3ea"></i><i style="background:#5a4a3a"></i><i style="background:#9a7a5a"></i><i style="background:#4a5a6a"></i><i style="background:#9aaab0"></i><i style="background:#7a7070"></i><i style="background:#b04030"></i><i style="background:#dfe3ea"></i><i style="background:#8a8070"></i>
    </div>
    <div class="sb-foot"><i></i>chatterloop social plugin</div>
  </div>
</section>

<footer class="abs site-footer">
  <div class="legal">Copyright 2013 <b>Murmurads</b>. All Right Reserved<span>|</span>Privacy Policy<span>|</span>FAQ<span>|</span>Terms</div>
  <div class="social"><i></i><i></i><i></i></div>
</footer>
</body>
</html>
```